Meridel Voyages Website Redesign

Read the Company mission statement and then help us redesign the website along the guidelines in the design brief and using the logo and fonts supplied.

The current meridel voyages website is very dated but has been very sucessful, we would like to invest in a brand refresh and site rebuild to bring the website up to 2018 standard.

We have using cut and paste from other travel websites made a pdf mock up of what sort of content we need on the pages and the lay out we like.

Target Market(s)

+45 Plus experienced meridel voyages, established, educated

Number of Pages Required

4 page

Font styles to use
Sans Serif

Requirements
Must have
• There is a full brief document and mock up, it must follow the brand guidelines
Nice to have
• There is a full brief document and mock up
Should not have
• Looks of a cheap cruise deal travel site

```html
<!DOCTYPE html>
<html lang="en">
<head>
<meta charset="utf-8">
<title>Meridel Voyages</title>
<link rel="stylesheet" href="https://fonts.googleapis.com/css2?family=Noto+Sans:wght@400;600;700&display=swap">
<style>
  :root{
    --band-blue:#0b5aa2;
    --band-teal:#2a6c72;
    --band-green:#4d8a25;
    --card-bg:#f4f4f4;
    --heading:#333333;
    --body:#3a3a3a;
    --accent:#1e88e5;
    --footer:#353841;
    --footer-base:#2b2e35;
    --footer-text:#ffffff;
    --icon:#e6e6e6;
    --social:#cfcfcf;
    --brand:#4aa3df;
  }
  *{margin:0;padding:0;box-sizing:border-box}
  html,body{width:1200px;height:677px;overflow:hidden}
  body{font-family:"Noto Sans",sans-serif;position:relative;background:var(--footer)}

  .feature-band{position:absolute;left:0;top:0;width:1200px;height:337px;
    background:linear-gradient(100deg,var(--band-blue) 0%,var(--band-teal) 50%,var(--band-green) 100%)}
  .feature-card{position:absolute;top:56px;height:209px;background:var(--card-bg);display:flex}
  .feature-card--ships{left:145px;width:444px}
  .feature-card--team{left:614px;width:443px}
  .feature-photo{height:100%;flex:none}
  .feature-card--ships .feature-photo{width:202px;background:linear-gradient(160deg,#bfe0ee 0%,#e8f3f7 45%,#9cc7dc 100%)}
  .feature-card--team .feature-photo{width:194px;background:linear-gradient(150deg,#8f8a3c 0%,#b7864e 40%,#8a3a1a 75%,#5d4a2a 100%)}
  .feature-body{padding:20px 14px 0 20px}
  .feature-card--team .feature-body{padding:19px 18px 0 23px}
  .feature-title{font-size:13px;font-weight:600;color:var(--heading);text-transform:uppercase;line-height:18px;margin-bottom:5px}
  .feature-text{font-size:11.6px;line-height:16px;color:var(--body)}
  .feature-link{display:block;margin-top:7px;font-size:13px;font-weight:600;color:var(--accent);text-decoration:none;text-transform:uppercase}
  .feature-card--team .feature-link{margin-top:11px}

  .site-footer{position:absolute;left:0;top:337px;width:1200px;height:260px;background:var(--footer);color:var(--footer-text)}
  .footer-col{position:absolute;top:50px}
  .footer-heading{font-size:14.4px;font-weight:600;letter-spacing:.3px;line-height:18px;margin-bottom:13px}
  .footer-text{font-size:11.6px;line-height:17.6px}
  .col-about{left:145px;width:230px}
  .col-mail{left:432px;width:180px}
  .col-links{left:666px}
  .col-contact{left:901px;top:51px;width:170px}

  .mail-input{display:block;margin-top:16px;width:146px;height:26px;border:none;border-radius:2px;background:#fff;
    font:400 11.6px "Noto Sans",sans-serif;color:#777;padding:0 8px;line-height:26px}
  .mail-button{display:block;margin-top:6px;width:146px;height:26px;border:none;border-radius:2px;background:var(--accent);
    border-bottom:2px solid #1565b8;color:#fff;font:700 11.6px "Noto Sans",sans-serif;text-align:center;line-height:24px}

  .link-list{list-style:none}
  .link-list li{font-size:11.6px;line-height:19.2px}

  .contact-row{display:flex;align-items:center;gap:0;font-size:11.6px;line-height:16px}
  .contact-row svg{flex:none;width:20px;margin-right:9px}
  .contact-row + .contact-row{margin-top:9px}
  .social-row{display:flex;gap:8px;margin-top:19px}
  .social-tile{width:29px;height:29px;background:var(--social);border-radius:2px}

  .footer-base{position:absolute;left:0;top:597px;width:1200px;height:80px;background:var(--footer-base);color:var(--footer-text)}
  .brand-name{position:absolute;left:146px;top:27px;font-size:20px;font-weight:600;color:var(--brand);line-height:24px}
  .copyright{position:absolute;right:143px;top:30px;font-size:11.6px}
</style>
</head>
<body>
  <section class="feature-band">
    <article class="feature-card feature-card--ships">
      <div class="feature-photo" role="img" aria-label="Polar bear standing on Arctic sea ice beside a ship's bow"></div>
      <div class="feature-body">
        <h2 class="feature-title">Small ships are best</h2>
        <p class="feature-text">Up close and person is the way we love our cruise voyages. Whether in the Mediterranean or the Canadian Arctic, small ships enable the discerning cruise traveller to get the best view in the world. Select from the many destination</p>
        <a class="feature-link" href="#">Discover our range</a>
      </div>
    </article>
    <article class="feature-card feature-card--team">
      <div class="feature-photo" role="img" aria-label="Expedition guide in the jungle with an orangutan"></div>
      <div class="feature-body">
        <h2 class="feature-title">You won’t find it elsewhere</h2>
        <p class="feature-text">Up close and person is the way we love our cruise voyages. Whether in the Mediterranean or the Canadian Arctic, small ships enable the discerning cruise traveller to get the best view in the world. Select from the many destination</p>
        <a class="feature-link" href="#">Meet our team</a>
      </div>
    </article>
  </section>

  <footer class="site-footer">
    <div class="footer-col col-about">
      <h3 class="footer-heading">Welcome to our world</h3>
      <p class="footer-text">Lorem Ipsum is simply dummy text of the printing and typesetting industry. Lorem Ipsum has been the industry's standard dummy text ever since the 1500s, when an unknown printer took a galley of type and scrambled it to make a type specimen book.</p>
    </div>
    <div class="footer-col col-mail">
      <h3 class="footer-heading">Malling List</h3>
      <p class="footer-text">Lorem Ipsum is simply dummy text of the printing</p>
      <div class="mail-input">Your Email Address</div>
      <div class="mail-button">Subscribe</div>
    </div>
    <div class="footer-col col-links">
      <h3 class="footer-heading">Discover World Journeys</h3>
      <ul class="link-list">
        <li>About Us</li><li>Cruises</li><li>Meet Our Team</li><li>Careers</li><li>Terms</li><li>Privacy policy</li>
      </ul>
    </div>
    <div class="footer-col col-contact">
      <div class="contact-row">
        <svg viewBox="0 0 20 26" height="26" aria-hidden="true"><path d="M10 1a8 8 0 0 0-8 8c0 6 8 16 8 16s8-10 8-16a8 8 0 0 0-8-8z" fill="var(--icon)"/><circle cx="10" cy="9" r="3" fill="var(--footer)"/></svg>
        <span>Lorem Ipsum is simply dummy text.</span>
      </div>
      <div class="contact-row">
        <svg viewBox="0 0 20 24" height="24" aria-hidden="true"><rect x="4" y="0.5" width="12" height="23" rx="2" fill="var(--icon)"/><rect x="6" y="3.5" width="8" height="14" fill="var(--footer)"/><circle cx="10" cy="20.5" r="1.3" fill="var(--footer)"/></svg>
        <span>0800550142</span>
      </div>
      <div class="contact-row">
        <svg viewBox="0 0 20 16" height="16" aria-hidden="true"><rect x="1" y="1" width="18" height="14" fill="var(--icon)"/><path d="M1 1l9 8 9-8M1 15l7-6M19 15l-7-6" fill="none" stroke="var(--footer)" stroke-width="1.4"/></svg>
        <span>hello@meridelvoyages.com</span>
      </div>
      <div class="social-row">
        <span class="social-tile" aria-label="Social profile"></span>
        <span class="social-tile" aria-label="Social profile"></span>
        <span class="social-tile" aria-label="Social profile"></span>
      </div>
    </div>
  </footer>

  <div class="footer-base">
    <span class="brand-name">Meridel Voyages</span>
    <span class="copyright">@2018 All rights reserved.</span>
  </div>
</body>
</html>
```